MOLT - Monitoring Natural Hazards from Space Web Application

KORVEN Sarl is a Luxembourg based Space-Startup that works in the field of Earth Observation. KORVEN is a platform able to extract value-added information from satellite data and is specialized in mapping Natural Disaster (floods, fires etc).

We are now developing a new vertical tool, called MOLT, dedicated to the monitoring of natural hazards in Humanitarian Camps around the world.

The goal of MOLT is to hide to the users' all the complexity of the Satellite Image processing and just provide them the results.

This project require to Design 4 pages of MOLT:
• Public Home Page (Code - V01)
• Dashboard (private Home Page) (Code - V03)
• Monitor (web GIS) (Code - V14)
• Registration Page (Code - V04)

We would like to provide the required time to make a good job.

Target Market(s)

Humanitarian Agencies, Goverments

Coding

Coded - Design and coding required

Number of Pages Required

4 page

Font styles to use
Other font styles liked:
• see the manual attached

Requirements
Must have
• 4 pages. One Home, one form, one dashboard and one web map.
Nice to have
• Please read the attachment with all the detailed instructions

```html
<!DOCTYPE html>
<html lang="en">
<head>
<meta charset="utf-8">
<title>MOLT Dashboard</title>
<link href="https://fonts.googleapis.com/css2?family=Inter:wght@400;500;600&display=swap" rel="stylesheet">
<style>
:root{
  --teal:#1f4a57;
  --teal-text:#24505e;
  --ink:#1d2329;
  --muted:#5b6670;
  --bg:#eef1f5;
  --panel:#f1f3f6;
  --line:#e2e6ea;
  --white:#ffffff;
  --map:#8fb0ef;
  --badge:#f2b92f;
  --danger:#e3141b;
}
*{box-sizing:border-box;margin:0;padding:0}
html,body{width:1200px;height:851px;overflow:hidden}
body{font-family:'Inter',sans-serif;background:var(--bg);color:var(--ink);position:relative}
.abs{position:absolute}
.sidebar{left:0;top:0;width:256px;height:851px;background:var(--white)}
.brand{left:32px;top:15px;display:flex;align-items:center;gap:12px;font-size:22px;font-weight:500;letter-spacing:5px;color:var(--teal-text)}
.brand-dot{width:30px;height:30px;border-radius:50%;border:2px solid var(--badge)}
.tab{top:76px;height:31px;display:flex;align-items:center;gap:7px;font-size:13px;padding:0 12px}
.tab.active{left:15px;width:112px;background:var(--teal);color:var(--white);border-radius:3px 3px 0 0}
.tab.plain{left:138px;color:var(--ink)}
.side-panel{left:15px;top:107px;width:228px;height:728px;background:var(--panel);border-radius:0 0 6px 6px}
.nav{left:33px;display:flex;align-items:center;gap:16px;font-size:11.5px;color:var(--teal-text);width:202px}
.nav svg{width:14px;height:14px;stroke:var(--teal-text);fill:none;stroke-width:1.6}
.nav.current{font-size:12.5px}
.nav-bar{left:15px;top:126px;width:2px;height:30px;background:var(--teal)}
.badge{margin-left:auto;width:15px;height:15px;border-radius:50%;background:var(--badge);font-size:7px;display:flex;align-items:center;justify-content:center;color:var(--ink)}
.side-divider{left:15px;top:675px;width:228px;height:1px;background:var(--line)}
.topbar{left:256px;top:0;width:944px;height:56px;background:var(--white)}
.page-title{left:277px;top:14px;display:flex;align-items:center;gap:8px;font-size:22px;color:var(--teal-text)}
.toggle{left:888px;top:20px;width:35px;height:15px;border-radius:3px;background:#e4e8ec}
.toggle span{position:absolute;left:0;top:0;width:17px;height:15px;background:var(--teal);border-radius:3px}
.lang{left:978px;top:20px;display:flex;align-items:center;gap:7px;font-size:9.5px}
.flag{width:22px;height:15px;background:linear-gradient(#2a3f8f,#2a3f8f);border:1px solid #c9cfe0;position:relative}
.flag::before{content:"";position:absolute;left:0;top:5px;width:20px;height:3px;background:#d4212d}
.user{left:1071px;top:8px;width:103px;height:40px;background:var(--panel);border-radius:4px;display:flex;align-items:center;gap:8px;padding-left:8px;font-size:10px}
.avatar{width:20px;height:20px;border-radius:50%;background:var(--ink)}
.h-overview{left:275px;top:77px;font-size:20px;color:var(--teal-text)}
.card{background:var(--white);border-radius:5px}
.card-title{font-size:15px;color:var(--teal-text)}
.select{background:var(--panel);border-radius:4px;display:flex;align-items:center;justify-content:space-between;padding:0 15px;font-size:9.5px;color:var(--muted)}
.map{left:284px;top:181px;width:877px;height:337px;background:var(--map);border-radius:3px}
.fs{left:1126px;top:191px;width:25px;height:27px;background:var(--white);border-radius:3px}
.dim{left:1025px;top:478px;width:126px;height:30px;background:var(--white);border-radius:3px;display:flex;overflow:hidden;font-size:10px}
.dim div{flex:1;display:flex;align-items:center;justify-content:center;gap:5px}
.dim .on{background:var(--teal);color:var(--white)}
.btn{background:var(--teal);color:var(--white);border-radius:3px;display:flex;align-items:center;justify-content:center;gap:6px;font-size:11px}
.btn-ghost{background:var(--panel);color:var(--muted);border-radius:3px;display:flex;align-items:center;justify-content:center;font-size:9px}
.box{border:1px solid var(--line);border-radius:4px;background:var(--white)}
.alert h4{font-size:11.5px;font-weight:400;margin-bottom:8px}
.alert p{font-size:8.5px;color:var(--muted)}
.scroll{width:1px;background:var(--line)}
.scroll span{display:block;width:2px;height:15px;background:var(--teal);margin-left:-0.5px}
</style>
</head>
<body>
<aside class="abs sidebar">
  <div class="abs brand"><span class="brand-dot"></span>MOLT</div>
  <div class="abs tab active"><svg width="12" height="12" viewBox="0 0 24 24" fill="none" stroke="#fff" stroke-width="2"><path d="M3 11l9-8 9 8v10h-6v-6H9v6H3z"/></svg>Dashboard</div>
  <div class="abs tab plain"><svg width="14" height="12" viewBox="0 0 24 24" fill="none" stroke="#1d2329" stroke-width="2"><path d="M2 12h4l3-7 5 14 3-7h5"/></svg>Monitor (GIS)</div>
  <div class="abs side-panel"></div>
  <div class="abs nav-bar"></div>
  <div class="abs nav current" style="top:134px"><svg viewBox="0 0 24 24"><rect x="3" y="4" width="18" height="16" rx="2"/><circle cx="12" cy="12" r="3"/></svg>Overview</div>
  <div class="abs nav" style="top:174px"><svg viewBox="0 0 24 24"><path d="M20 12a8 8 0 1 1-3-6.2M20 4v5h-5"/></svg>Updates and Alerts<span class="badge">35</span></div>
  <div class="abs nav" style="top:214px"><svg viewBox="0 0 24 24"><circle cx="12" cy="12" r="3"/><circle cx="12" cy="12" r="8" stroke-dasharray="4 2"/></svg>Settings</div>
  <div class="abs side-divider"></div>
  <div class="abs nav" style="top:694px"><svg viewBox="0 0 24 24"><circle cx="12" cy="12" r="9"/><path d="M9.5 9.5a2.5 2.5 0 1 1 3 2.5v2M12 17h.01"/></svg>Help Centre</div>
  <div class="abs nav" style="top:734px"><svg viewBox="0 0 24 24"><path d="M12 21s-8-3-8-10a8 8 0 0 1 16 0c0 7-8 10-8 10z"/><path d="M10 9a2 2 0 1 1 2 2v1"/></svg>Contact us</div>
  <div class="abs nav" style="top:774px"><svg viewBox="0 0 24 24"><path d="M9 4H4v16h5M16 8l4 4-4 4M20 12H9"/></svg>Logout</div>
</aside>

<header class="abs topbar"></header>
<div class="abs page-title"><svg width="22" height="22" viewBox="0 0 24 24" fill="none" stroke="#24505e" stroke-width="2"><path d="M3 11l9-8 9 8v10h-6v-6H9v6H3z"/></svg>Dashboard</div>
<div class="abs toggle"><span></span></div>
<svg class="abs" style="left:943px;top:20px" width="14" height="15" viewBox="0 0 24 24" fill="none" stroke="#1d2329" stroke-width="2"><path d="M6 16V10a6 6 0 0 1 12 0v6l2 2H4zM10 21h4"/></svg>
<div class="abs lang"><span class="flag"></span>English <svg width="9" height="9" viewBox="0 0 24 24" fill="none" stroke="#1d2329" stroke-width="2.5"><path d="M6 9l6 6 6-6"/></svg></div>
<div class="abs user"><span class="avatar"></span>Norvale <svg width="9" height="9" viewBox="0 0 24 24" fill="none" stroke="#1d2329" stroke-width="2.5"><path d="M6 9l6 6 6-6"/></svg></div>

<h1 class="abs h-overview" style="font-weight:400">Overview</h1>

<section class="abs card" style="left:274px;top:116px;width:897px;height:457px">
  <h2 class="abs card-title" style="left:10px;top:20px;font-weight:400">Areas of Operation</h2>
  <div class="abs select" style="left:755px;top:15px;width:132px;height:29px">Area 1 <svg width="9" height="9" viewBox="0 0 24 24" fill="none" stroke="#5b6670" stroke-width="2.5"><path d="M6 9l6 6 6-6"/></svg></div>
  <div class="abs" style="left:10px;top:50px;width:877px;height:1px;background:var(--line)"></div>
  <div class="abs btn" style="left:10px;top:417px;width:88px;height:30px"><svg width="13" height="11" viewBox="0 0 24 24" fill="none" stroke="#fff" stroke-width="2"><path d="M2 12h4l3-7 5 14 3-7h5"/></svg>Monitor</div>
</section>
<div class="abs map" role="img" aria-label="World map of operation areas with markers for flooded zones and people affected"></div>
<div class="abs fs"><svg style="margin:7px" width="11" height="11" viewBox="0 0 24 24" fill="none" stroke="#1d2329" stroke-width="2.5"><path d="M3 8V3h5M16 3h5v5M21 16v5h-5M8 21H3v-5"/></svg></div>
<div class="abs dim"><div class="on">▯ 2D</div><div>◯ 3D</div></div>

<section class="abs card" style="left:274px;top:588px;width:292px;height:243px">
  <h2 class="abs card-title" style="left:10px;top:22px;font-weight:500">Affected People</h2>
  <div class="abs select" style="left:189px;top:15px;width:93px;height:29px">All Areas <svg width="9" height="9" viewBox="0 0 24 24" fill="none" stroke="#5b6670" stroke-width="2.5"><path d="M6 9l6 6 6-6"/></svg></div>
  <div class="abs" style="left:10px;top:50px;width:272px;height:1px;background:var(--line)"></div>
  <div class="abs box" style="left:10px;top:60px;width:272px;height:76px">
    <p class="abs" style="left:10px;top:11px;font-size:11px">Total People Affected</p>
    <p class="abs" style="left:10px;top:35px;font-size:26px;font-weight:500;color:var(--teal-text)">1.200.136</p>
  </div>
  <div class="abs btn" style="left:10px;top:203px;width:88px;height:30px">View on map</div>
</section>

<section class="abs card" style="left:577px;top:588px;width:291px;height:243px;overflow:hidden">
  <h2 class="abs card-title" style="left:10px;top:22px;font-weight:400">Events Ongoing</h2>
  <div class="abs select" style="left:188px;top:15px;width:93px;height:29px">All Areas <svg width="9" height="9" viewBox="0 0 24 24" fill="none" stroke="#5b6670" stroke-width="2.5"><path d="M6 9l6 6 6-6"/></svg></div>
  <div class="abs" style="left:10px;top:50px;width:272px;height:1px;background:var(--line)"></div>
  <div class="abs box" style="left:10px;top:61px;width:261px;height:127px">
    <p class="abs" style="left:10px;top:11px;font-size:8.5px;color:var(--muted)">Area 1</p>
    <p class="abs" style="left:10px;top:27px;font-size:12px">Flood Detected in Area 1</p>
    <p class="abs" style="left:10px;top:50px;font-size:8.5px">On : 14/09/2024</p>
    <p class="abs" style="left:10px;top:73px;font-size:8.5px;display:flex;align-items:center;gap:6px">Severity : <span style="width:10px;height:10px;border-radius:50%;background:var(--danger)"></span>High Risk</p>
    <div class="abs btn" style="left:10px;top:92px;width:72px;height:24px;font-size:9px">Open Map</div>
    <div class="abs btn-ghost" style="left:87px;top:92px;width:77px;height:24px">View details</div>
  </div>
  <div class="abs box" style="left:10px;top:196px;width:261px;height:60px">
    <p class="abs" style="left:10px;top:11px;font-size:8.5px;color:var(--muted)">Area 2</p>
    <p class="abs" style="left:10px;top:27px;font-size:12px">Fire Detected in Area 2</p>
  </div>
  <div class="abs scroll" style="left:280px;top:60px;height:175px"><span></span></div>
</section>

<section class="abs card" style="left:879px;top:588px;width:292px;height:243px">
  <h2 class="abs card-title" style="left:10px;top:22px;font-weight:400">Alerts</h2>
  <div class="abs select" style="left:189px;top:15px;width:93px;height:29px">Latest <svg width="9" height="9" viewBox="0 0 24 24" fill="none" stroke="#5b6670" stroke-width="2.5"><path d="M6 9l6 6 6-6"/></svg></div>
  <div class="abs" style="left:10px;top:50px;width:272px;height:1px;background:var(--line)"></div>
  <div class="abs box alert" style="left:10px;top:57px;width:261px;height:52px;padding:11px 10px"><h4>Heavy Rain in Area 1</h4><p>12498 people are affected by this.</p></div>
  <div class="abs box alert" style="left:10px;top:119px;width:261px;height:52px;padding:11px 10px"><h4>Fire Rain in Area 2</h4><p>854 people are affected by this fire.</p></div>
  <div class="abs box alert" style="left:10px;top:181px;width:261px;height:52px;padding:11px 10px"><h4>Heavy Rain in Area 3</h4><p>498 people are affected by this.</p></div>
  <div class="abs scroll" style="left:280px;top:60px;height:175px"><span></span></div>
</section>
</body>
</html>
```